Redone of Site on Wix

Project Overview: Website Redesign for Brovanta
We are looking to redesign our current website, www.brovantausa.com, to better match the style and functionality of these reference sites:
Quorin Health
MZT FlexBit
Key Requirements: Modern, Clean Design:
The site should have a professional and clean layout with clear messaging about our services.
Visual Elements: Use strong visuals like images, icons, or illustrations to support text and engage visitors.
Clear Service Breakdown: Easily digestible sections explaining what Brovanta offers, similar to the service explanations on the reference sites.
User-Friendly Navigation: Simple, intuitive navigation with visible CTAs (e.g., "Learn More," "Get Started").
Trust-Building Features: Incorporate trust elements like client logos, testimonials, or success stories to build credibility.
Mobile-Responsive:
Ensure the website is fully responsive and looks great on all devices (desktop, tablet, mobile).
SEO Optimization:
Deliverables: Fully functional website with modern design.
All content will be provided, but we may need help with imagery or layout recommendations.
Responsive design and mobile optimization.
We are looking for a clean, modern, and easy-to-navigate site that reflects the professionalism of our brand.

```html
<!DOCTYPE html>
<html lang="en">
<head>
<meta charset="utf-8">
<title>Brovanta – Medical Food for Sickle Cell Disease</title>
<link href="https://fonts.googleapis.com/css2?family=Rubik:wght@400;500;600;700;800&display=swap" rel="stylesheet">
<style>
:root{
  --red:#b3242a;
  --red-dark:#9c1d23;
  --ink:#1d1d1f;
  --muted:#5b5b5f;
  --line:#e4e4e6;
  --field:#f1f1f2;
  --footer:#231f20;
  --gold:#f4c41a;
  --icon-bg:#f6e3e3;
  --white:#ffffff;
}
*{box-sizing:border-box;margin:0;padding:0}
html,body{width:1200px;height:3504px;overflow:hidden}
body{position:relative;font-family:'Rubik',Arial,sans-serif;color:var(--ink);background:var(--white)}
.abs{position:absolute}
a{color:inherit;text-decoration:none}

/* top bar + nav */
.topbar{left:0;top:0;width:1200px;height:30px;background:var(--red);color:var(--white);font-size:12px;display:flex;justify-content:flex-end;align-items:center;gap:14px;padding-right:144px}
.nav{left:0;top:30px;width:1200px;height:56px;background:var(--white)}
.brand{position:absolute;left:143px;top:8px;color:var(--red);font-size:34px;font-weight:500;letter-spacing:1px;line-height:34px}
.brand small{display:block;font-size:6px;letter-spacing:0;color:var(--red);line-height:8px}
.menu{position:absolute;left:392px;top:20px;display:flex;gap:29px;font-size:15px;color:var(--ink)}
.menu .active{position:relative}
.menu .active::after{content:"";position:absolute;left:26px;right:26px;top:24px;height:2px;background:var(--red)}

/* hero */
.hero{left:0;top:86px;width:1200px;height:580px;overflow:hidden}
.hero-photo{position:absolute;inset:0;background:linear-gradient(100deg,#eceae6 0%,#e3ddd6 38%,#c9a58f 58%,#8d6a58 78%,#e9e3dc 100%)}
.hero-curve{position:absolute;left:0;bottom:0}
.hero h1{position:absolute;left:143px;top:92px;font-size:64px;font-weight:800;letter-spacing:1px;color:#111}
.hero p{position:absolute;left:144px;top:184px;width:440px;font-size:16px;line-height:30px;color:#111}
.btn{display:inline-flex;align-items:center;justify-content:center;background:var(--red);color:var(--white);border-radius:30px;font-weight:500;text-transform:uppercase}
.hero .btn{position:absolute;left:143px;top:274px;width:166px;height:46px;font-size:16px}

/* partner logos */
.logo-box{top:735px;width:218px;height:70px;border:1px solid var(--line);display:flex;align-items:center;justify-content:center;gap:10px;font-size:23px;font-weight:600;color:#222}
.logo-box i{display:block;width:28px;height:28px;border-radius:50%;background:#222}
.round-arrow{width:30px;height:30px;border-radius:50%;box-shadow:0 1px 6px rgba(0,0,0,.18);background:var(--white);display:flex;align-items:center;justify-content:center}

/* section titles */
.title{left:0;width:1200px;text-align:center;font-weight:700;font-size:36px;letter-spacing:.5px}
.rule{height:3px;background:var(--red)}

/* solution cards */
.sol-card{top:969px;width:442px;height:299px;background:var(--white);box-shadow:0 2px 14px rgba(0,0,0,.08);border-radius:6px}
.sol-icon{position:absolute;left:24px;top:22px;width:72px;height:72px;border-radius:50%;background:var(--icon-bg)}
.sol-card h3{position:absolute;left:22px;top:114px;width:400px;font-size:18px;font-weight:400;line-height:28px}
.sol-card p{position:absolute;left:22px;top:185px;width:404px;font-size:13.5px;line-height:23px;color:var(--muted)}
.dark-arrow{width:34px;height:34px;border-radius:50%;background:#3a3a3c;display:flex;align-items:center;justify-content:center}

/* testimonials */
.clients{left:0;top:1355px;width:1200px;height:699px;background:linear-gradient(135deg,#b3242a 0%,#a21f25 50%,#b3242a 100%)}
.client{top:1603px;width:215px;height:306px;background:var(--white);border-radius:2px;text-align:center}
.avatar-ring{position:absolute;left:43px;top:-62px;width:128px;height:128px;border-radius:50%;background:var(--white);border:3px solid var(--red);clip-path:inset(0 0 50% 0)}
.avatar{position:absolute;left:53px;top:-52px;width:108px;height:108px;border-radius:50%;background:linear-gradient(160deg,#d8d2cc,#9b8b7f)}
.client h4{position:absolute;left:0;width:100%;top:78px;font-size:18px;font-weight:400}
.client p{position:absolute;left:20px;width:175px;top:116px;font-size:12.5px;line-height:24px;color:var(--muted)}
.socials{position:absolute;left:0;width:100%;top:262px;display:flex;justify-content:center;gap:12px}
.socials span{width:20px;height:20px;border-radius:50%;border:1px solid #ccc;font-size:10px;font-weight:700;display:flex;align-items:center;justify-content:center;color:#222}
.outline-btn{left:528px;top:1948px;width:139px;height:41px;border:2px solid var(--white);border-radius:22px;color:var(--white);font-size:14px;font-weight:500;display:flex;align-items:center;justify-content:center}

/* offers */
.offer{top:2258px;width:434px;height:281px;background:var(--white);box-shadow:0 2px 18px rgba(0,0,0,.08);text-align:center}
.offer .tag{position:absolute;top:44px;width:100%;font-size:11px;color:var(--red)}
.offer .name{position:absolute;top:66px;width:100%;font-size:19px;color:#444}
.offer .price{position:absolute;top:100px;width:100%;font-size:25px;font-weight:700}
.offer .price b{color:var(--red)}
.offer hr{position:absolute;left:22px;right:22px;top:148px;border:0;border-top:1px solid var(--line)}
.offer .desc{position:absolute;top:171px;width:100%;font-size:14px;color:var(--muted)}
.offer .btn{position:absolute;left:145px;top:214px;width:146px;height:38px;font-size:14px}
.ribbon{position:absolute;right:-16px;top:-24px}

/* contact form */
.field{height:45px;background:var(--field);border-radius:2px;display:flex;align-items:center;gap:8px;padding-left:19px;font-size:13px;color:#8a8a8e}
.field.area{align-items:flex-start;padding-top:16px}
.submit{left:532px;top:3001px;width:136px;height:38px;font-size:14px}

/* footer */
.footer{left:0;top:3122px;width:1200px;height:382px}
.footer-brand{left:143px;top:3248px;color:var(--white);font-size:54px;font-weight:400;letter-spacing:2px;line-height:54px}
.footer-brand small{display:block;font-size:7px;letter-spacing:0;line-height:10px}
.f-social{top:3338px;width:34px;height:34px;border-radius:50%;background:var(--white);color:var(--footer);font-size:13px;font-weight:700;display:flex;align-items:center;justify-content:center}
.f-col h5{font-size:17px;font-weight:400;color:var(--white);margin-bottom:12px}
.f-col li{list-style:none;color:var(--white);font-size:12.5px;line-height:30.5px;display:flex;align-items:center;gap:10px}
.f-col li em{color:var(--red);font-style:normal;font-size:11px}
.copy{left:0;top:3472px;width:1200px;text-align:center;color:var(--white);font-size:12.5px}
.footline{left:143px;top:3456px;width:914px;height:1px;background:#3a3536}
</style>
</head>
<body>

<div class="abs topbar">
  <span>✉&nbsp; info@brovanta.com</span><span>|</span><span>☎&nbsp; +1-555-014-2290</span>
</div>

<header class="abs nav">
  <div class="brand">Brovanta<small>(nutritional formula for daily dietary care)</small></div>
  <nav class="menu">
    <a class="active">About BROVANTA</a><a>About SCD</a><a>Healthcare Professionals</a><a>Patient Support</a><a>Veyra Sciences</a>
  </nav>
</header>

<section class="abs hero">
  <div class="hero-photo" role="img" aria-label="Smiling mother feeding her young daughter at a kitchen table with fresh fruit"></div>
  <svg class="hero-curve" width="1200" height="130" viewBox="0 0 1200 130">
    <path d="M0 60 Q600 200 1200 40 L1200 130 L0 130Z" fill="#fff"/>
    <path d="M0 50 Q600 170 1200 30 L1200 40 Q600 190 0 60Z" fill="#b3242a"/>
  </svg>
  <h1>BROVANTA</h1>
  <p>A Medical Food For The Dietary Managemnt of Sickle Cell Diseas In Pediatric and Patients.</p>
  <a class="btn">Get Started</a>
</section>

<div class="abs round-arrow" style="left:79px;top:755px"><svg width="10" height="10"><path d="M7 1 L2 5 L7 9Z" fill="#222"/></svg></div>
<div class="abs logo-box" style="left:143px"><i></i>logoipsum</div>
<div class="abs logo-box" style="left:374px"><i></i>logoipsum</div>
<div class="abs logo-box" style="left:605px"><i></i>logoipsum</div>
<div class="abs logo-box" style="left:837px"><i></i>logoipsum</div>
<div class="abs round-arrow" style="left:1090px;top:755px"><svg width="10" height="10"><path d="M3 1 L8 5 L3 9Z" fill="#222"/></svg></div>

<h2 class="abs title" style="top:890px">THE BROVANTA SOLUTION</h2>
<div class="abs dark-arrow" style="left:73px;top:1101px"><svg width="12" height="12"><path d="M8 1 L3 6 L8 11" stroke="#fff" stroke-width="1.8" fill="none"/></svg></div>
<article class="abs sol-card" style="left:146px">
  <div class="sol-icon" role="img" aria-label="Digestion icon"></div>
  <h3>Fat Malabsorption is a top contributor to Digestive /GI problems.</h3>
  <p>Lorem ipsum dolor sit amet, consectetur adipiscing elit, sed do eiusmod tempor incididunt ut labore et dolore magna aliqua. Ut enim ad minim veniam, quis nostrud exercitation ullamco laboris nisi ut aliquip ex ea commodo consequat.</p>
</article>
<article class="abs sol-card" style="left:613px">
  <div class="sol-icon" role="img" aria-label="Health care icon"></div>
  <h3>GI-related health care expenses exceed $135 billion each year. 1</h3>
  <p>Lorem ipsum dolor sit amet, consectetur adipiscing elit, sed do eiusmod tempor incididunt ut labore et dolore magna aliqua. Ut enim ad minim veniam, quis nostrud exercitation ullamco laboris nisi ut aliquip ex ea commodo consequat.</p>
</article>
<div class="abs dark-arrow" style="left:1092px;top:1101px"><svg width="12" height="12"><path d="M4 1 L9 6 L4 11" stroke="#fff" stroke-width="1.8" fill="none"/></svg></div>

<section class="abs clients" role="img" aria-label="Red-tinted photo of a smiling man in a warehouse"></section>
<h2 class="abs title" style="top:1428px;color:#fff">WHAT OUR CLIENTS ARE SAYING</h2>
<div class="abs rule" style="left:517px;top:1492px;width:160px;background:#fff"></div>

<div class="abs client" style="left:143px"><div class="avatar-ring"></div><div class="avatar" role="img" aria-label="Portrait of Jhone Duo"></div><h4>Jhone Duo</h4><p>Lorem ipsum dolor sit amet, consectetur adipiscing elit, sed do eiusmod tempor incididunt ut labore et dolore magna aliqua.</p><div class="socials"><span>f</span><span>in</span><span>◎</span></div></div>
<div class="abs client" style="left:375px"><div class="avatar-ring"></div><div class="avatar" role="img" aria-label="Portrait of Melina Jersy"></div><h4>Melina Jersy</h4><p>Lorem ipsum dolor sit amet, consectetur adipiscing elit, sed do eiusmod tempor incididunt ut labore et dolore magna aliqua.</p><div class="socials"><span>f</span><span>in</span><span>◎</span></div></div>
<div class="abs client" style="left:607px"><div class="avatar-ring"></div><div class="avatar" role="img" aria-label="Portrait of Gold Berg"></div><h4>Gold Berg</h4><p>Lorem ipsum dolor sit amet, consectetur adipiscing elit, sed do eiusmod tempor incididunt ut labore et dolore magna aliqua.</p><div class="socials"><span>f</span><span>in</span><span>◎</span></div></div>
<div class="abs client" style="left:839px"><div class="avatar-ring"></div><div class="avatar" role="img" aria-label="Portrait of Natasha"></div><h4>Natasha</h4><p>Lorem ipsum dolor sit amet, consectetur adipiscing elit, sed do eiusmod tempor incididunt ut labore et dolore magna aliqua.</p><div class="socials"><span>f</span><span>in</span><span>◎</span></div></div>
<a class="abs outline-btn">LEARN MORE</a>

<h2 class="abs title" style="top:2130px">OUR OFFERS</h2>
<div class="abs rule" style="left:556px;top:2192px;width:96px"></div>

<div class="abs offer" style="left:137px">
  <svg class="ribbon" width="132" height="92" viewBox="0 0 132 92"><path d="M0 22 L14 22 L14 10Z" fill="#c9a00e"/><path d="M110 92 L110 78 L122 78Z" fill="#c9a00e"/><path d="M14 22 L40 0 L122 78 L110 92Z" fill="#f4c41a"/><text x="72" y="46" transform="rotate(42 72 46)" font-family="Rubik,Arial,sans-serif" font-size="13" font-weight="700" text-anchor="middle" fill="#222">BASIC</text></svg>
  <div class="tag">OFFER 01</div><div class="name">Lorem Ipsum</div>
  <div class="price"><b>$19.99</b>/WEEK</div><hr>
  <div class="desc">Sed ut perspiciatis unde omnis iste natus error</div>
  <a class="btn">Learn More</a>
</div>
<div class="abs offer" style="left:614px">
  <svg class="ribbon" width="132" height="92" viewBox="0 0 132 92"><path d="M0 22 L14 22 L14 10Z" fill="#c9a00e"/><path d="M110 92 L110 78 L122 78Z" fill="#c9a00e"/><path d="M14 22 L40 0 L122 78 L110 92Z" fill="#f4c41a"/><text x="72" y="46" transform="rotate(42 72 46)" font-family="Rubik,Arial,sans-serif" font-size="13" font-weight="700" text-anchor="middle" fill="#222">PREMIUM</text></svg>
  <div class="tag">OFFER 02</div><div class="name">Lorem Ipsum</div>
  <div class="price"><b>$90.99</b>/MONTH</div><hr>
  <div class="desc">Sed ut perspiciatis unde omnis iste natus error</div>
  <a class="btn">Learn More</a>
</div>

<h2 class="abs title" style="top:2618px;font-weight:500">CONTACT US</h2>
<div class="abs rule" style="left:552px;top:2682px;width:96px"></div>
<form>
  <div class="abs field" style="left:180px;top:2725px;width:409px">👤 First Name</div>
  <div class="abs field" style="left:611px;top:2725px;width:408px">👤 Last Name</div>
  <div class="abs field" style="left:180px;top:2794px;width:409px">✉ Email Address</div>
  <div class="abs field" style="left:611px;top:2794px;width:408px">📍 Location</div>
  <div class="abs field area" style="left:180px;top:2864px;width:838px;height:103px">💬 Message</div>
  <button class="abs btn submit" style="border:0;font-family:inherit">Submit Now</button>
</form>

<svg class="abs footer" width="1200" height="382" viewBox="0 0 1200 382">
  <path d="M0 90 Q600 -60 1200 90 L1200 382 L0 382Z" fill="#b3242a"/>
  <path d="M0 116 Q600 -30 1200 116 L1200 382 L0 382Z" fill="#231f20"/>
</svg>
<div class="abs footer-brand">Brovanta<small>(nutritional formula for daily dietary care)</small></div>
<div class="abs f-social" style="left:202px">f</div>
<div class="abs f-social" style="left:245px">◎</div>
<div class="abs f-col" style="left:533px;top:3226px">
  <h5>QUICK LINKS</h5>
  <ul><li><em>»</em>About BROVANTA</li><li><em>»</em>About SCD</li><li><em>»</em>Healthcare Professionals</li><li><em>»</em>Patient Support</li><li><em>»</em>Veyra Sciences</li><li><em>»</em>Contact</li></ul>
</div>
<div class="abs f-col" style="left:872px;top:3226px">
  <h5>CONTACT US</h5>
  <ul><li><em>●</em>176 Lorem Ipsum Site Amet</li><li><em>▯</em>+1-555-014-2290</li><li><em>✉</em>info@brovanta.com</li></ul>
</div>
<div class="abs footline"></div>
<div class="abs copy">© 2025 &nbsp;Brovanta &nbsp;| &nbsp;All Rights Reserved</div>

</body>
</html>
```